Advert for Services that we offer

Brindle Forge Ltd need an design to represent what we do in a modern way by showing an image with a brief description and the use of corporate logo the information we will proved vie a doc file and this is to be presented in a modern way. This design will be for print & web. we have done our own design and its not great i have put this in the file repository

Target Market(s)

Motor trade

Font styles to use
Sans Serif

Colors

Designer to choose colors to be used in the design.

Requirements
Must have
• Company colour scheme as per logo within the files uploaded.
• and a small boarder to isolate it from the rest of the articles.
Nice to have
• Modern font
Should not have
• Old style font

```html
<!DOCTYPE html>
<html lang="en">
<head>
<meta charset="utf-8">
<title>Brindle Forge Ltd – Product Testing &amp; Analysis</title>
<link rel="stylesheet" href="https://fonts.googleapis.com/css2?family=Orbitron:wght@700;900&family=Roboto+Condensed:wght@400;500;700&display=swap">
<style>
  :root {
    --brand-blue: #1a6cc2;
    --brand-blue-dark: #0f4f9e;
    --brand-blue-light: #3d9ae6;
    --steel-grey: #9b9ea3;
    --silver: #d8dadd;
    --white: #ffffff;
    --photo-dark: #4a4f57;
    --photo-orange: #d4592a;
  }
  html, body {
    margin: 0;
    padding: 0;
    width: 1200px;
    height: 827px;
    overflow: hidden;
    background: var(--white);
  }
  .advert {
    position: relative;
    width: 1200px;
    height: 827px;
    overflow: hidden;
    background: var(--white);
    font-family: "Roboto Condensed", Arial, sans-serif;
    box-sizing: border-box;
    border: 3px solid var(--brand-blue);
  }
  .advert__shapes {
    position: absolute;
    inset: 0;
  }
  .headline {
    position: absolute;
    left: 28px;
    top: 38px;
    margin: 0;
    font-family: "Orbitron", Arial, sans-serif;
    font-weight: 900;
    font-size: 62px;
    letter-spacing: 1px;
    color: var(--brand-blue);
    white-space: nowrap;
  }
  .company-name {
    position: absolute;
    right: 26px;
    top: 160px;
    display: flex;
    align-items: center;
    gap: 12px;
    font-family: "Roboto Condensed", Arial, sans-serif;
    font-weight: 700;
    font-size: 30px;
    color: var(--brand-blue);
    white-space: nowrap;
  }
  .company-name__square {
    width: 34px;
    height: 34px;
    background: var(--brand-blue);
  }
  .web-address {
    position: absolute;
    left: 228px;
    top: 155px;
    display: flex;
    align-items: center;
    gap: 14px;
    color: var(--white);
    font-size: 27px;
    font-weight: 400;
  }
  .service-list {
    position: absolute;
    left: 50px;
    top: 212px;
    margin: 0;
    padding: 0;
    list-style: none;
  }
  .service-list__item {
    display: flex;
    align-items: center;
    height: 82px;
    gap: 28px;
    color: var(--white);
    font-size: 44px;
    font-weight: 500;
    white-space: nowrap;
  }
  .service-list__icon {
    width: 72px;
    height: 72px;
    flex: none;
  }
  .phone {
    position: absolute;
    left: 48px;
    top: 738px;
    display: flex;
    align-items: center;
    gap: 22px;
    font-family: "Orbitron", Arial, sans-serif;
    font-weight: 700;
    font-size: 48px;
    color: var(--white);
    white-space: nowrap;
  }
  .social {
    position: absolute;
    left: 650px;
    top: 700px;
    color: var(--brand-blue);
  }
  .social__label {
    font-size: 34px;
    font-weight: 400;
    margin: 0 0 8px;
  }
  .social__links {
    display: flex;
    gap: 10px;
  }
  .social__square {
    width: 30px;
    height: 30px;
    border-radius: 4px;
    background: var(--brand-blue);
  }
</style>
</head>
<body>
<main class="advert">
  <svg class="advert__shapes" width="1200" height="827" viewBox="0 0 1200 827">
    <defs>
      <linearGradient id="panel-gradient" x1="0" y1="0" x2="1" y2="1">
        <stop offset="0" stop-color="#1560b8"/>
        <stop offset="0.55" stop-color="#3c97e4"/>
        <stop offset="1" stop-color="#1a6cc2"/>
      </linearGradient>
      <linearGradient id="footer-gradient" x1="0" y1="0" x2="1" y2="0">
        <stop offset="0" stop-color="#c9ccd0"/>
        <stop offset="1" stop-color="#eef0f2"/>
      </linearGradient>
      <linearGradient id="photo-gradient" x1="0" y1="0" x2="1" y2="1">
        <stop offset="0" stop-color="#c9c9c9"/>
        <stop offset="0.45" stop-color="#7b7f86"/>
        <stop offset="0.8" stop-color="#d4592a"/>
        <stop offset="1" stop-color="#3d4149"/>
      </linearGradient>
    </defs>

    <!-- grey accent strip -->
    <polygon class="accent-strip" points="0,168 190,168 160,212 0,212" fill="var(--steel-grey)"/>

    <!-- main service panel -->
    <path class="service-panel" d="M0,212 H160 L190,150 H860 L745,490 Q733,520 752,545 L905,700 H0 Z" fill="url(#panel-gradient)"/>
    <!-- inner edge line -->
    <path class="service-panel__edge" d="M835,162 L722,495 Q712,520 730,545 L870,690" fill="none" stroke="var(--brand-blue-dark)" stroke-width="10" opacity="0.6"/>

    <!-- web address bar -->
    <polygon class="web-bar" points="190,150 860,150 848,196 170,196" fill="var(--brand-blue-dark)"/>

    <!-- service row bands -->
    <g class="service-bands" fill="#ffffff" opacity="0.08">
      <rect x="90" y="222" width="560" height="60"/>
      <rect x="90" y="304" width="600" height="60"/>
      <rect x="90" y="386" width="560" height="60"/>
      <rect x="90" y="468" width="620" height="60"/>
      <rect x="90" y="550" width="640" height="60"/>
    </g>

    <!-- footer band -->
    <path class="footer-band" d="M0,700 H905 L940,735 L960,827 H0 Z" fill="url(#footer-gradient)"/>

    <!-- phone bar -->
    <path class="phone-bar" d="M0,720 H570 Q590,720 600,735 L640,827 H0 Z" fill="var(--brand-blue)"/>

    <!-- workshop photo area -->
    <path class="workshop-photo" role="img" aria-label="Photo: technician measuring a bore with a dial gauge in the workshop"
      d="M870,250 H1200 V770 H1005 L775,545 Q758,520 770,495 Z" fill="url(#photo-gradient)"/>
  </svg>

  <h1 class="headline">PRODUCT TESTING &amp; ANALYSIS</h1>

  <div class="company-name"><span class="company-name__square"></span>Brindle Forge Ltd</div>

  <div class="web-address">
    <svg width="30" height="30" viewBox="0 0 30 30" fill="none" stroke="#fff" stroke-width="2">
      <circle cx="15" cy="15" r="12"/>
      <ellipse cx="15" cy="15" rx="5.5" ry="12"/>
      <line x1="3" y1="15" x2="27" y2="15"/>
      <line x1="5" y1="9" x2="25" y2="9"/>
      <line x1="5" y1="21" x2="25" y2="21"/>
    </svg>
    <span>www.brindle-forge.co.uk</span>
  </div>

  <ul class="service-list">
    <li class="service-list__item">
      <svg class="service-list__icon" viewBox="0 0 72 72">
        <rect x="14" y="14" width="44" height="44" transform="rotate(45 36 36)" fill="#c8ccd1" stroke="#eef0f2" stroke-width="3"/>
        <path d="M26,44 V32 L36,25 L46,32 V44 H40 V37 H32 V44 Z" fill="var(--brand-blue)"/>
      </svg>
      Metallurgical testing
    </li>
    <li class="service-list__item">
      <svg class="service-list__icon" viewBox="0 0 72 72">
        <rect x="14" y="14" width="44" height="44" transform="rotate(45 36 36)" fill="#c8ccd1" stroke="#eef0f2" stroke-width="3"/>
        <circle cx="36" cy="36" r="11" fill="none" stroke="var(--brand-blue)" stroke-width="4"/>
        <circle cx="36" cy="36" r="4" fill="var(--brand-blue)"/>
      </svg>
      Bearing pre-load testing
    </li>
    <li class="service-list__item">
      <svg class="service-list__icon" viewBox="0 0 72 72">
        <rect x="14" y="14" width="44" height="44" transform="rotate(45 36 36)" fill="#c8ccd1" stroke="#eef0f2" stroke-width="3"/>
        <circle cx="31" cy="34" r="8" fill="var(--brand-blue)"/>
        <rect x="31" y="38" width="18" height="6" fill="var(--brand-blue)"/>
      </svg>
      Bore measurement
    </li>
    <li class="service-list__item">
      <svg class="service-list__icon" viewBox="0 0 72 72">
        <rect x="14" y="14" width="44" height="44" transform="rotate(45 36 36)" fill="#c8ccd1" stroke="#eef0f2" stroke-width="3"/>
        <rect x="27" y="25" width="16" height="22" fill="none" stroke="var(--brand-blue)" stroke-width="2.5"/>
        <line x1="30" y1="31" x2="40" y2="31" stroke="var(--brand-blue)" stroke-width="2"/>
        <line x1="30" y1="36" x2="40" y2="36" stroke="var(--brand-blue)" stroke-width="2"/>
        <line x1="38" y1="44" x2="47" y2="30" stroke="var(--brand-blue)" stroke-width="3"/>
      </svg>
      New product evaluation
    </li>
    <li class="service-list__item">
      <svg class="service-list__icon" viewBox="0 0 72 72">
        <rect x="14" y="14" width="44" height="44" transform="rotate(45 36 36)" fill="#c8ccd1" stroke="#eef0f2" stroke-width="3"/>
        <rect x="27" y="36" width="4" height="10" fill="var(--brand-blue)"/>
        <rect x="33" y="32" width="4" height="14" fill="var(--brand-blue)"/>
        <rect x="39" y="34" width="4" height="12" fill="var(--brand-blue)"/>
        <polyline points="26,32 33,26 39,30 46,24" fill="none" stroke="var(--brand-blue)" stroke-width="2.5"/>
      </svg>
      Product analysis &amp; report
    </li>
  </ul>

  <div class="phone">
    <svg width="44" height="44" viewBox="0 0 44 44" fill="none" stroke="#fff" stroke-width="3" stroke-linecap="round">
      <path d="M10,6 L16,6 L19,14 L15,17 Q18,25 27,29 L30,25 L38,28 L38,34 Q38,38 33,38 Q8,36 6,11 Q6,6 10,6 Z" fill="#fff" stroke="none"/>
      <path d="M27,8 Q35,10 36,18"/>
      <path d="M26,14 Q30,15 30,19"/>
    </svg>
    <span>(0161) 496 0721</span>
  </div>

  <div class="social">
    <p class="social__label">Follow us</p>
    <div class="social__links">
      <span class="social__square"></span>
      <span class="social__square"></span>
      <span class="social__square"></span>
      <span class="social__square"></span>
    </div>
  </div>
</main>
</body>
</html>
```